Consulting firm needs a professional letterhead design

We need a professional letterhead design which is simple but unique. It should carry attributes of the latest designs in the market suitable for professional environmental consultancies.

- The logo is attached for you to USE.
- Our preferred color scheme is that shown in the logo.
- Letterhead text color is your choice to make.
- Logo to the left and text to the right plus slogan/tagline is desirable for this letterhead.

Use any address etc. of your choice in the letterhead.

Target Market(s)

Consulting firms and government agencies

Industry/Entity Type

Environmental Consultant

Colors
acd037
fece3e
85cae6
3277b5

Requirements
Must have
• Logo supplied and color scheme must be used.
Nice to have
• Nexa font is used in the Logo, so it would ne nice to have nexa font in the letterhead too.

```html
<!DOCTYPE html>
<html lang="en">
<head>
<meta charset="utf-8">
<title>Terravane Letterhead</title>
<link href="https://fonts.googleapis.com/css2?family=Lato:wght@400;700;900&family=Great+Vibes&display=swap" rel="stylesheet">
<style>
  :root{
    --green:#acd037;
    --yellow:#fece3e;
    --sky:#85cae6;
    --blue:#3277b5;
    --ink:#4a4a4a;
    --navy:#1f2a44;
    --muted:#666666;
    --backdrop:#c9cacb;
    --paper:#ffffff;
  }
  *{box-sizing:border-box;margin:0;padding:0}
  html,body{width:1200px;height:1091px;overflow:hidden}
  body{background:var(--backdrop);font-family:"Lato",Arial,sans-serif;color:var(--ink)}
  .letterhead{
    position:absolute;left:213px;top:45px;width:773px;height:1000px;
    background:var(--paper);box-shadow:0 6px 18px rgba(0,0,0,.15);overflow:hidden;
  }
  .top-accent{position:absolute;right:0;top:0}
  .contact{position:absolute;right:70px;top:52px;list-style:none;font-size:10px;line-height:15px;color:var(--muted)}
  .contact li{display:flex;align-items:center;gap:6px}
  .contact svg{flex:none}
  .brand{position:absolute;left:70px;top:108px;display:flex;align-items:center;gap:12px}
  .brand-dot{width:30px;height:30px;border-radius:50%;background:var(--blue);flex:none}
  .brand-name{font-weight:900;font-size:26px;letter-spacing:2px;color:var(--navy);line-height:1}
  .brand-tagline{font-size:10.5px;color:var(--navy);margin-top:3px;letter-spacing:.3px}
  .letter{position:absolute;left:96px;top:218px;width:590px;font-size:13px;line-height:20px}
  .salutation{font-weight:700;margin-bottom:20px}
  .letter p{margin-bottom:20px}
  .closing{margin-top:10px}
  .signature{font-family:"Great Vibes",cursive;font-size:34px;color:var(--blue);margin-top:6px;line-height:1.1}
  .address{position:absolute;right:40px;bottom:28px;font-size:10px;color:#555;display:flex;align-items:center;gap:5px}
  .bottom-accent{position:absolute;left:0;bottom:0}
</style>
</head>
<body>
  <main class="letterhead">
    <svg class="top-accent" width="240" height="40" viewBox="0 0 240 40" aria-hidden="true">
      <defs>
        <linearGradient id="topGrad" x1="0" x2="1">
          <stop offset="0" stop-color="#fece3e"/>
          <stop offset="1" stop-color="#acd037"/>
        </linearGradient>
      </defs>
      <polygon points="0,10 240,0 240,6 30,14" fill="url(#topGrad)"/>
      <polygon points="170,0 240,0 240,8 150,8" fill="#acd037"/>
    </svg>

    <ul class="contact">
      <li><svg width="9" height="9" viewBox="0 0 10 10"><circle cx="5" cy="5" r="5" fill="#3277b5"/></svg>014-562-3870</li>
      <li><svg width="9" height="9" viewBox="0 0 10 10"><rect width="10" height="7" y="1.5" rx="1" fill="#3277b5"/></svg>info@terravane.com</li>
      <li><svg width="9" height="9" viewBox="0 0 10 10"><circle cx="5" cy="5" r="4.3" fill="none" stroke="#3277b5" stroke-width="1.4"/></svg>www.terravane.com</li>
    </ul>

    <header class="brand">
      <span class="brand-dot"></span>
      <div>
        <div class="brand-name">TERRAVANE</div>
        <div class="brand-tagline">Bridging research and sound policy</div>
      </div>
    </header>

    <section class="letter">
      <div class="salutation">Dear Mr. Lorem,</div>
      <p>Lorem ipsum dolor sit amet, consectetuer adipiscing elit, sed diam nonummy nibh euismod tincidunt ut laoreet dolore magna aliquam erat volutpat. Ut wisi enim ad minim veniam, quis nostrud exerci tation ullamcorper suscipit lobortis nisl ut aliquip ex ea commodo consequat. Duis autem vel eum iriure dolor in hendiusto odio dignissim qui blandit praesent luptatum zzril delenit augue duis dolore te feugait nulla facilisi.</p>
      <p>Lorem ipsum dolor sit amet, consectetuer adipiscing elit, sed diam nonummy nibh euismod tincidunt ut laoreet dolore magna aliquam erat volutpat. Ut wisi enim ad minim veniam, quis nostrud exerci tation ullamcorper suscipit lobortis nisl ut aliquip ex ea commodo consequat. Duis autem vel eum iriure dolor in hendiusto odio dignissim qui blandit praesent luptatum zzril delenit augue duis dolore te feugait nulla facilisi.</p>
      <p>Lorem ipsum dolor sit amet, consectetuer adipiscing elit, sed diam nonummy nibh euismod tincidunt ut laoreet dolore magna aliquam erat volutpat. Ut wisi enim ad minim veniam, quis nostrud exerci tation ullamcorper suscipit lobortis nisl ut aliquip ex ea commodo consequat. Duis autem vel eum iriure dolor in hendiusto odio dignissim qui blandit praesent luptatum zzril delenit augue duis dolore te feugait nulla facilisi.</p>
      <div class="closing">Sincerely Your,</div>
      <div class="signature">Your Name</div>
    </section>

    <div class="address">
      <svg width="9" height="11" viewBox="0 0 10 12"><path d="M5 0a4 4 0 0 1 4 4c0 3-4 8-4 8S1 7 1 4a4 4 0 0 1 4-4z" fill="#3277b5"/><circle cx="5" cy="4" r="1.5" fill="#fff"/></svg>
      111, Street Name, City Name, State Name - 012345
    </div>

    <svg class="bottom-accent" width="773" height="18" viewBox="0 0 773 18" aria-hidden="true">
      <defs>
        <linearGradient id="bottomGrad" x1="0" x2="1">
          <stop offset="0" stop-color="#3277b5"/>
          <stop offset="1" stop-color="#85cae6"/>
        </linearGradient>
      </defs>
      <rect x="0" y="13" width="773" height="5" fill="#3277b5"/>
      <polygon points="560,13 773,2 773,13" fill="url(#bottomGrad)"/>
    </svg>
  </main>
</body>
</html>
```